Flyer-Design für Hochzeitswebseiten
Zielgruppe
Wir machen Hochzeitswebseiten ( www.saveyourdaylight.de).
Aufgabenstellung
Gerne hätte ich folgendes DIN Format: 210x148 quer mit 6 Seiten. 1 Seite schwarz mit unserem Logo. 2 Seite Bild. 3 Seite Text. 4 Seite 4-5 Bilder. 5 Seite Text. 6 Seite Kontaktinformationen.
Text1:
Ihr habt alles dafür getan, dass Eure Hochzeit so schön wie möglich wird. Wir tun alles dafür, dass die Erinnerung daran so großartig wie möglich bleibt. Ihr stellt uns Eure persönlichen Informationen und Fotos zur Verfügung. Wir machen daraus eine professionelle Website über den schönsten Tag Eures Lebens. Ihr entscheidet über Umfang und Budget.
Wir widmen uns jedem Auftrag mit Begeisterung und Kreativität.
Text2: evtl. sollte da das Basic und Premiumpaket beschrieben werden. Sind uns da aber unsicher.

```html
<!DOCTYPE html>
<html lang="de">
<head>
<meta charset="utf-8">
<title>Save Your Daylight – Flyer Außenseite</title>
<link rel="stylesheet" href="https://fonts.googleapis.com/css2?family=Cardo:wght@400;700&family=Cinzel:wght@400&family=Marcellus&display=swap">
<style>
  :root {
    --paper: #000000;
    --gold: #9a7420;
    --gold-bright: #c9a13a;
    --ink: #ffffff;
  }
  * { margin: 0; padding: 0; box-sizing: border-box; }
  html, body {
    width: 1200px; height: 285px; overflow: hidden;
    background: var(--paper);
  }
  .flyer {
    position: relative; width: 1200px; height: 285px;
    background: var(--paper); color: var(--ink);
    font-family: "Marcellus", "Cardo", Georgia, serif;
  }

  /* Price packages */
  .package__title {
    position: absolute; top: 37px;
    color: var(--gold); font-family: "Cardo", Georgia, serif;
    font-weight: 700; font-size: 9.6px; line-height: 12px; letter-spacing: 0.03em;
  }
  .package__price {
    position: absolute; font-size: 8.4px; line-height: 10px; white-space: nowrap;
  }
  .package__price small { font-size: 4.8px; }
  .package__features {
    position: absolute; list-style: none;
    font-size: 8.3px; line-height: 9.62px; white-space: nowrap;
  }
  .package__features .gap { height: 9.62px; }
  .package__extra {
    position: absolute;
    color: var(--gold); font-family: "Cardo", Georgia, serif;
    font-weight: 700; font-size: 8px; line-height: 10px; white-space: nowrap;
  }

  .basic .package__title { left: 38px; top: 37px; }
  .basic .package__price { left: 38px; top: 58px; }
  .basic .package__features { left: 46px; top: 78px; }
  .basic .package__extra { left: 38px; top: 240px; }

  .premium .package__title { left: 240px; top: 36px; }
  .premium .package__price { left: 240px; top: 57px; }
  .premium .package__features { left: 248px; top: 77px; }
  .premium .package__extra { left: 240px; top: 241px; }

  /* Contact panel */
  .contact-panel {
    position: absolute; left: 500px; width: 250px; top: 0; height: 285px;
    text-align: center;
  }
  .brand-small {
    position: absolute; top: 68px; left: 0; width: 100%;
    color: var(--gold-bright); font-size: 15px; line-height: 18px;
  }
  .contact-panel__title {
    position: absolute; top: 152px; left: 0; width: 100%;
    color: var(--gold); font-family: "Cinzel", Georgia, serif;
    font-weight: 400; font-size: 14.5px; line-height: 18px;
  }
  .contact-panel__lines {
    position: absolute; top: 185.5px; left: 0; width: 100%;
    font-size: 11px; line-height: 13px; white-space: nowrap;
  }

  /* Cover */
  .brand-large {
    position: absolute; left: 850px; width: 314px; top: 126px;
    text-align: center; color: var(--gold-bright);
    font-size: 30px; line-height: 36px; white-space: nowrap;
  }
</style>
</head>
<body>
<main class="flyer">
  <section class="package basic">
    <h2 class="package__title">BASIC</h2>
    <p class="package__price">299.- Euro (einmalig) <small>inkl. MwSt</small></p>
    <ul class="package__features">
      <li>50GB Speicherplatz</li>
      <li>50 Fotos</li>
      <li>Eine Wunschdomain</li>
      <li>Eigene E-Mailadresse</li>
      <li>Passwortschutz</li>
      <li>SSL Zertifikat</li>
      <li class="gap" aria-hidden="true"></li>
      <li>Keine Werbung</li>
      <li>Optimiert für Smartphones und Tablets</li>
      <li>Keine Verpflichtungen</li>
      <li>Keine automatische Verlängerung</li>
      <li>Eure Webseite als ZIP-Datei</li>
      <li>Hosting &amp; Serverkosten für 1 Jahr</li>
    </ul>
    <p class="package__extra">Auf Wunsch: Save the Date</p>
  </section>

  <section class="package premium">
    <h2 class="package__title">PREMIUM</h2>
    <p class="package__price">429.- Euro (einmalig) <small>inkl. MwSt</small></p>
    <ul class="package__features">
      <li>Unbegrenzter Speicherplatz</li>
      <li>Unbegrenzte Anzahl an Fotos</li>
      <li>Euer Hochzeitsvideo</li>
      <li>Eine Wunschdomain</li>
      <li>Eigene E-Mailadresse</li>
      <li>Ausführliche Berichte</li>
      <li>Gästebuch</li>
      <li>Verknüpfung Socialnet &amp; Picstream</li>
      <li>Passwortschutz</li>
      <li>SSL-Zertifikat</li>
      <li>Keine Werbung</li>
      <li>Optimiert für Smartphones und Tablets</li>
      <li>Keine Verpflichtungen</li>
      <li>Keine automatische Verlängerung</li>
      <li>Eure Webseite als ZIP-Datei</li>
      <li>Hosting &amp; Serverkosten für 1 Jahr</li>
    </ul>
    <p class="package__extra">Auf Wunsch: Save the Date</p>
  </section>

  <section class="contact-panel">
    <p class="brand-small">Save Your Daylight</p>
    <h1 class="contact-panel__title">SAVE YOUR DAYLIGHT</h1>
    <p class="contact-panel__lines">
      Telefon +49 (0) 221 55 01 23 45<br>
      Email: info@saveyourdaylight.de<br>
      Website: www.saveyourdaylight.de
    </p>
  </section>

  <p class="brand-large">Save Your Daylight</p>
</main>
</body>
</html>
```